Two Marketing Brochures

We need two professional A4 brochures (PDF + web version) to promote our new handyman services to Facility Managers in Queensland.
Brochure 1: BRW Facilities Trade Services (see content BRW Facilities.pdf). Create new cover page and contents page then design 2 content pages (left and right) I will then paste all text myself, rather than designing 19 pages.
Brochure 2: BRW Facilities Minor Works & Maintenance – Smarter, Simpler, Cheaper
Audience: Commercial property managers, QLD Gov, councils, schools, industrial clients
Style: Clean, modern, corporate, BRW Facilities-branded
Content: Text is finalised and ready to go
Deliverables: A4 PDF (print-ready) + web version (compressed)
Optional: Integration of TaskLoop7 elements (e.g. “Book Now” QR or icon)

```html
<!DOCTYPE html>
<html lang="en">
<head>
<meta charset="utf-8">
<title>BRW Facilities – Trade Services Catalogue</title>
<link href="https://fonts.googleapis.com/css2?family=Montserrat:wght@300;400;500;600;700;800;900&display=swap" rel="stylesheet">
<style>
  :root{
    --stage:#dadada;
    --navy:#1d3a5c;
    --ink:#3a3f47;
    --panel:#f3f2ee;
    --label:#dcdcdc;
    --dot:#2b2b2b;
    --white:#ffffff;
  }
  *{margin:0;padding:0;box-sizing:border-box}
  html,body{width:1200px;height:1200px;overflow:hidden;background:var(--stage);font-family:"Montserrat",sans-serif;color:var(--ink)}
  .page{position:absolute;width:333px;height:471px;background:var(--white);overflow:hidden}
  .page--cover{left:251px;top:113px;background:var(--navy)}
  .page--contents{left:616px;top:113px}
  .page--charge{left:251px;top:616px}
  .page--electrical{left:616px;top:616px}

  /* cover */
  .cover-photo{position:absolute;left:0;top:0;width:333px;height:376px;background:linear-gradient(160deg,#3d4f66 0%,#2b3a4e 45%,#4a3e36 75%,#26334a 100%)}
  .cover-photo::after{content:"";position:absolute;right:0;top:0;width:90px;height:80px;background:radial-gradient(circle at 80% 20%,rgba(214,190,40,.55),rgba(214,190,40,0) 70%)}
  .wordmark{position:absolute;font-weight:600;letter-spacing:.04em;color:var(--white);display:flex;align-items:center;gap:5px}
  .wordmark__dot{width:.75em;height:.75em;border-radius:50%;background:var(--white)}
  .cover .wordmark{left:24px;top:30px;font-size:13px}
  .cover-title{position:absolute;left:24px;top:293px;font-weight:900;font-size:16.5px;line-height:18.5px;color:var(--white);letter-spacing:.01em}
  .cover-sub{position:absolute;left:24px;top:340px;font-weight:300;font-size:10.6px;line-height:12.6px;color:#e6eaf0;letter-spacing:.02em}
  .cover-tag{position:absolute;left:24px;top:389px;font-weight:700;font-size:8.6px;line-height:10.6px;color:var(--white)}
  .cover-blurb{position:absolute;left:24px;top:417px;width:172px;font-weight:600;font-size:5.6px;line-height:7.4px;color:var(--white)}
  .badge{position:absolute;top:418px;width:29px;height:29px;border-radius:50%;background:var(--white);border:2.5px solid var(--white)}
  .badge::after{content:"";position:absolute;inset:5px;border-radius:50%}
  .badge--red{left:211px}.badge--red::after{background:#d42a2a}
  .badge--green{left:246px}.badge--green::after{background:#2e9a3e}
  .badge--gold{left:281px}.badge--gold::after{background:#f1bf1f}

  /* inner page header */
  .page-header{position:absolute;left:24px;right:0;top:12px;height:36px;background:var(--navy)}
  .page-header .wordmark{right:24px;top:11px;font-size:9.5px}
  .page-title{position:absolute;left:24px;top:58px;font-weight:700;font-size:8.3px;color:var(--navy);letter-spacing:.02em}
  .page-footer{position:absolute;right:24px;bottom:9px;font-size:4.3px;color:#5a6b80}

  /* contents */
  .toc{position:absolute;left:24px;right:24px;top:0;list-style:none}
  .toc__row{position:absolute;left:0;right:0;height:10px;display:flex;align-items:center;gap:6px;font-size:5.6px;letter-spacing:.02em;color:var(--ink)}
  .toc__row--section{font-weight:700;color:var(--navy)}
  .toc__rule{flex:1;height:.5px;background:#8a93a0}
  .toc__num{width:9.5px;height:9.5px;border-radius:50%;background:var(--dot);color:var(--white);font-size:4.8px;font-weight:500;display:flex;align-items:center;justify-content:center}
  .toc__row--section .toc__num{background:var(--navy)}

  /* charge table */
  .intro{position:absolute;left:24px;top:69px;font-size:5.3px;color:var(--ink)}
  .intro strong{color:var(--navy)}
  .table{position:absolute;left:24px;width:285px;display:flex;border-bottom:1px solid var(--white)}
  .table__label{width:110px;background:var(--label);display:flex;align-items:center;padding-left:11px;font-weight:600;font-size:6px;color:var(--navy)}
  .table__body{flex:1;background:var(--panel);padding:5px 8px 5px 12px;font-size:4.2px;line-height:5.2px;display:flex;flex-direction:column;justify-content:center}

  /* electrical */
  .svc-head{position:absolute;left:24px;width:285px;height:23.5px;background:var(--navy);color:var(--white);font-weight:700;font-size:7.4px;display:flex;align-items:center;justify-content:center;letter-spacing:.02em}
  .svc-row{position:absolute;left:24px;width:285px;display:flex;border-top:1px solid var(--white)}
  .svc-row .table__label{width:78px;font-size:6px}
  .svc-row .table__body{padding:4px 8px 4px 12px;font-size:4.1px;line-height:6.1px}
  .svc-list{list-style:none}
  .svc-list li{position:relative;padding-left:6px}
  .svc-list li::before{content:"-";position:absolute;left:0}
</style>
</head>
<body>

<!-- Cover -->
<section class="page page--cover cover">
  <div class="cover-photo" role="img" aria-label="Photo of trade tools on a dark workbench: hammer, wrenches, tape measure, leather gloves and a yellow hard hat"></div>
  <div class="wordmark"><span class="wordmark__dot"></span>BRW FACILITIES</div>
  <h1 class="cover-title">TRADE SERVICES<br>CATALOGUE</h1>
  <p class="cover-sub">APPLIANCES, PLUMBING,<br>ELECTRICAL, HEATING &amp; COOLING</p>
  <p class="cover-tag">LEGENDARY &nbsp;SERVICE,<br>DELIVERED DAILY</p>
  <p class="cover-blurb">BRW is Plumbing, Electrical, Heating, and Cooling on demand. With easy bookings, solid van tracking door-to-door, and goodlooking reports, we're guaranteed to get the job done.</p>
  <span class="badge badge--red"></span>
  <span class="badge badge--green"></span>
  <span class="badge badge--gold"></span>
</section>

<!-- Contents -->
<section class="page page--contents">
  <div class="page-header"><div class="wordmark"><span class="wordmark__dot"></span>BRW FACILITIES</div></div>
  <h2 class="page-title">CONTENTS</h2>
  <ol class="toc">
    <li class="toc__row toc__row--section" style="top:83px">HOW WE CHARGE<span class="toc__rule"></span><span class="toc__num">3</span></li>
    <li class="toc__row toc__row--section" style="top:96px">SERVICE POLICY<span class="toc__rule"></span><span class="toc__num">4</span></li>
    <li class="toc__row toc__row--section" style="top:109px">SERVICE OVERVIEW - ELECTRICAL<span class="toc__rule"></span><span class="toc__num">5</span></li>
    <li class="toc__row" style="top:120.5px">APPLIANCE INSPECTION (ELECTRICAL, GAS, WATER)<span class="toc__rule"></span><span class="toc__num">5</span></li>
    <li class="toc__row" style="top:132px">ELECTRICAL SAFETY INSPECTION<span class="toc__rule"></span><span class="toc__num">5</span></li>
    <li class="toc__row" style="top:143.5px">SMOKE ALARM COMPLIANCE INSPECTION<span class="toc__rule"></span><span class="toc__num">6</span></li>
    <li class="toc__row" style="top:155px">THERMAL IMAGING – SWITCHBOARDS<span class="toc__rule"></span><span class="toc__num">6</span></li>
    <li class="toc__row" style="top:166.5px">LIGHT SWITCH REPLACEMENT<span class="toc__rule"></span><span class="toc__num">7</span></li>
    <li class="toc__row" style="top:178px">POWERPOINT REPLACEMENT<span class="toc__rule"></span><span class="toc__num">7</span></li>
    <li class="toc__row" style="top:189.5px">CEILING EXHAUST FAN REPLACEMENT<span class="toc__rule"></span><span class="toc__num">8</span></li>
    <li class="toc__row" style="top:201px">DOWN LIGHT REPLACEMENT<span class="toc__rule"></span><span class="toc__num">8</span></li>
    <li class="toc__row toc__row--section" style="top:214px">SERVICE OVERVIEW - PLUMBING<span class="toc__rule"></span><span class="toc__num">9</span></li>
    <li class="toc__row" style="top:225.5px">GAS SAFETY INSPECTION<span class="toc__rule"></span><span class="toc__num">9</span></li>
    <li class="toc__row" style="top:237px">FLEXI HOSE INSPECTION<span class="toc__rule"></span><span class="toc__num">9</span></li>
    <li class="toc__row" style="top:248.5px">HOT WATER FAULTS<span class="toc__rule"></span><span class="toc__num">10</span></li>
    <li class="toc__row" style="top:260px">TEMPORARY HOT WATER INSTALLATION<span class="toc__rule"></span><span class="toc__num">11</span></li>
    <li class="toc__row" style="top:271.5px">MAJOR BLOCKAGE (Storm and Sewer)<span class="toc__rule"></span><span class="toc__num">11</span></li>
    <li class="toc__row" style="top:283px">ROOF LEAK AND ASSESSMENT<span class="toc__rule"></span><span class="toc__num">12</span></li>
    <li class="toc__row" style="top:294.5px">LEAK DETECTION - Minor Waste Blockages (Sink, Basin, Shower, etc.)<span class="toc__rule"></span><span class="toc__num">13</span></li>
    <li class="toc__row toc__row--section" style="top:307.5px">SERVICE OVERVIEW – HEATING &amp; COOLING<span class="toc__rule"></span><span class="toc__num">14</span></li>
    <li class="toc__row" style="top:319px">AC SPLIT SYSTEM INSPECTION &amp; DIAGNOSIS<span class="toc__rule"></span><span class="toc__num">14</span></li>
    <li class="toc__row" style="top:330.5px">AC SPLIT SYSTEM SERVICE/INSPECTION<span class="toc__rule"></span><span class="toc__num">14</span></li>
    <li class="toc__row" style="top:342px">AC SPLIT SYSTEM HYDRO CLEAN<span class="toc__rule"></span><span class="toc__num">15</span></li>
    <li class="toc__row" style="top:353.5px">GAS 'DUCTED' HEATING SERVICE/INSPECTION<span class="toc__rule"></span><span class="toc__num">15</span></li>
    <li class="toc__row" style="top:365px">TEMPORARY HEATING/COOLING<span class="toc__rule"></span><span class="toc__num">16</span></li>
    <li class="toc__row toc__row--section" style="top:378px">CUSTOMER TERMS OF SERVICE<span class="toc__rule"></span><span class="toc__num">17</span></li>
    <li class="toc__row toc__row--section" style="top:391px">SERVICE CHARGES<span class="toc__rule"></span><span class="toc__num">19</span></li>
    <li class="toc__row" style="top:402.5px">Electrical<span class="toc__rule"></span><span class="toc__num">19</span></li>
    <li class="toc__row" style="top:414px">Heating &amp; Cooling<span class="toc__rule"></span><span class="toc__num">19</span></li>
    <li class="toc__row" style="top:425.5px">Plumbing<span class="toc__rule"></span><span class="toc__num">19</span></li>
    <li class="toc__row" style="top:437px">Appliances<span class="toc__rule"></span><span class="toc__num">19</span></li>
  </ol>
  <p class="page-footer">BRW Facility Services Pty Ltd 2025</p>
</section>

<!-- How we charge -->
<section class="page page--charge">
  <div class="page-header"><div class="wordmark"><span class="wordmark__dot"></span>BRW FACILITIES</div></div>
  <h2 class="page-title">HOW WE CHARGE</h2>
  <p class="intro">We have simplified charging to <strong>3 different modes</strong> - so you always have control over your costs.</p>
  <div class="table" style="top:84px;height:32px">
    <div class="table__label">Mode #1: Do and Charge</div>
    <div class="table__body">This is when nobody is sure what a problem is and what needs to be done. Think of it as a general service, where we send a plumber, electrician, or heating &amp; cooling specialist to site and attempt to make repairs, whatever they are.</div>
  </div>
  <div class="table" style="top:116px;height:42px">
    <div class="table__label">Mode #2: Flat Rate Service</div>
    <div class="table__body">In the following pages, we have listed our standard services with a fixed price. This way, you will know exactly what you will pay for these services, and they are exactly as described. If there is any variation or addition to these costs, we will not proceed without authorised approval.</div>
  </div>
  <div class="table" style="top:158px;height:48px">
    <div class="table__label">Mode #3: Quote</div>
    <div class="table__body">Where a job can be clearly scoped, and no additional technical information is required, we will provide a free quote for your consideration. We will attend the site and take negotiated measurements. If a fault-finding or technical assessment is required on-site before a quote is submitted, then we will need to attend as a 'do and charge.'</div>
  </div>
  <p class="page-footer">BRW Facility Services Pty Ltd 2025</p>
</section>

<!-- Electrical overview -->
<section class="page page--electrical">
  <div class="page-header"><div class="wordmark"><span class="wordmark__dot"></span>BRW FACILITIES</div></div>
  <h2 class="page-title">SERVICE OVERVIEW - ELECTRICAL</h2>

  <div class="svc-head" style="top:74px">APPLIANCE INSPECTION (ELECTRICAL, GAS, WATER)</div>
  <div class="svc-row" style="top:97.5px;height:55.5px">
    <div class="table__label">Works Include</div>
    <div class="table__body"><ul class="svc-list">
      <li>Testing and diagnosis of appliance issue.</li>
      <li>Minor repairs where economical to do so.</li>
      <li>Report detailing the appliance issue or repairs made.</li>
      <li>Quotation for replacement of appliance if beyond reasonable and practical repair.</li>
      <li>Photos: before and after.</li>
      <li>Removal and disposal of all rubbish related to works.</li>
      <li>Area cleaned upon completion of work.</li>
    </ul></div>
  </div>
  <div class="svc-row" style="top:153px;height:80px">
    <div class="table__label">Important Notes</div>
    <div class="table__body"><ul class="svc-list">
      <li>To test and work on appliances, all appliances must be readily accessible. If we must wait an extended time for an appliance to become accessible to test (e.g., someone is using the appliance, or an oven is too hot to work on), additional hourly charges will be incurred.</li>
      <li>All appliances/equipment must be reasonably accessible and in a clean environment. Example: Technicians cannot move dirty/clean dishes or laundry to access an appliance. Technicians require clear access to an appliance and a clean working area.</li>
      <li>No responsibility is taken for goods damaged while working (glasses, crockery, towel, etc.) if they are not moved in preparation for the technician to complete their work.</li>
    </ul></div>
  </div>

  <div class="svc-head" style="top:243px">ELECTRICAL SAFETY INSPECTION</div>
  <div class="svc-row" style="top:266.5px;height:56px">
    <div class="table__label">Works Include</div>
    <div class="table__body">Testing of all accessible parts of the electrical installation, including:<ul class="svc-list">
      <li>Visual inspection.</li>
      <li>Mandatory testing in accordance with AS/NZS:3019:2022.</li>
      <li>Audit report showing compliance and/or defect list.</li>
      <li>Photos: before and after.</li>
      <li>Removal and disposal of all rubbish related to works.</li>
      <li>Area cleaned upon completion of work.</li>
    </ul></div>
  </div>
  <div class="svc-row" style="top:322.5px;height:67px">
    <div class="table__label">Important Notes</div>
    <div class="table__body"><ul class="svc-list">
      <li>If any part of the electrical installation is found to present clear and immediate danger to property or persons, then we will disconnect that appliance or part of the installation from supply and quote for remedial works later.</li>
      <li>All parts of the installation and equipment must be reasonably accessible and in a clean environment. Example: Technicians cannot crawl under renters' tables or around/over furniture to access light fixtures, power outlets, smoke alarms, nor can we be expected to move dirty dishes/glasses/appliances, etc., to access appliances.</li>
      <li>Power must be connected to the property.</li>
    </ul></div>
  </div>
  <p class="page-footer">BRW Facility Services Pty Ltd 2025</p>
</section>

</body>
</html>
```